High Quality Hemp Flowers Packaging Design

We need a logo and packaging design for a new CBD hemp product. We sell CBD rich hemp flower- tops to our customers in Europe. CBD's natural benefits are extensive and generally used for all sorts of reasons.
Our strains are of the highest quality and used as an aromatic product. Thus the design should look clean and modern with a slight organic touch. We'd like people to associate our product with a luxury product like a good wine or whiskey but still being modern, healthy and organic.
The product comes in a brown cardboard paper tube and the design needs to include:
-our logo made of the "miren amulett" (attachment 1 miren amulett)
-our website: "dolvik.eu"
-the product name: "miren"
tube properties:
tube size: 6cm diameter, 7cm height (please see attachment 2 Paper Tube 6cm diameter, 7cm height. jpg)
• material: 2mm thickness cardboard+brown kraft paper (like in attachment 3 Paper Tube colour.jpg – picture just a sample for the material – size is not correctly displayed in this picture)
• coated aluminum foil paper inside
• colour/ product name: whatever colour and where ever you want to place it in your design
• colour/ miren amulet logo: whatever colour and where ever you want to place it in your design
• sticker (2-2.5 x 5-6,5cm –> whatever the designer thinks works better) for sealing use, to keep the two parts of the tube together and it needs to have a placeholder for the date of the packaging (like in attachment 2 Paper Tube 6cm diameter 7cm height – but the sticker will not cover the full side of the tube as in attachment 2, but just 5-6.5 cm)
• “inner” tube could be color printing (for clarification which part please see attachment 3 Paper Tube colour.jpg -> the white part – picture just a sample for the “white part” – size is not correctly displayed in this picture
- We dont need any marihuana leafs or signs.

```html
<!DOCTYPE html>
<html lang="en">
<head>
<meta charset="utf-8">
<title>miren – CBD Rich Hemp Flower</title>
<link rel="stylesheet" href="https://fonts.googleapis.com/css2?family=Montserrat:wght@400;500;600&display=swap">
<style>
  :root {
    --canvas-bg: #ffffff;
    --tube-green: #21441f;
    --tube-green-edge: #2c4f2a;
    --tube-green-light: #4a6e4a;
    --opening-shade: #173317;
    --gold-dark: #a8781f;
    --gold-mid: #d9ad52;
    --gold-light: #f3dc95;
    --band-text: #2a3a1e;
  }
  * { margin: 0; padding: 0; box-sizing: border-box; }
  html, body {
    width: 1200px;
    height: 1200px;
    overflow: hidden;
    background: var(--canvas-bg);
  }
  .canvas {
    position: relative;
    width: 1200px;
    height: 1200px;
    background: var(--canvas-bg);
  }
  .tube {
    position: absolute;
    left: 422px;
    top: 250px;
    width: 354px;
    height: 838px;
    border-radius: 22px 22px 14px 14px / 18px 18px 10px 10px;
    background: linear-gradient(90deg,
      var(--tube-green-edge) 0%,
      var(--tube-green) 6%,
      var(--tube-green) 30%,
      var(--tube-green-light) 50%,
      var(--tube-green) 68%,
      var(--tube-green) 86%,
      var(--tube-green-light) 100%);
    font-family: "Montserrat", sans-serif;
    overflow: hidden;
  }
  .tube-opening {
    position: absolute;
    left: 48px;
    top: 22px;
    width: 262px;
    height: 22px;
    border-radius: 50%;
    background: var(--opening-shade);
    box-shadow: inset 0 4px 6px rgba(0,0,0,0.35);
  }
  .brand-seal {
    position: absolute;
    left: 64px;
    top: 134px;
    width: 212px;
    height: 212px;
    border: 3px solid var(--gold-mid);
    border-radius: 50%;
    display: flex;
    align-items: center;
    justify-content: center;
  }
  .brand-name {
    font-size: 50px;
    font-weight: 600;
    color: var(--gold-mid);
    letter-spacing: 1px;
    line-height: 1;
  }
  .product-band {
    position: absolute;
    left: 0;
    right: 0;
    top: 364px;
    height: 48px;
    background: linear-gradient(90deg, var(--gold-dark) 0%, var(--gold-light) 45%, var(--gold-mid) 75%, var(--gold-dark) 100%);
    display: flex;
    align-items: center;
    justify-content: center;
  }
  .product-name {
    font-size: 24px;
    font-weight: 400;
    color: var(--band-text);
    white-space: nowrap;
  }
  .leaf-art {
    position: absolute;
    left: 46px;
    top: 454px;
    width: 246px;
    height: 220px;
    border-radius: 50%;
    background: radial-gradient(ellipse at 50% 45%, var(--gold-light) 0%, var(--gold-mid) 45%, rgba(168,120,31,0) 75%);
  }
  .website {
    position: absolute;
    left: 0;
    right: 0;
    top: 704px;
    text-align: center;
    font-size: 16px;
    font-weight: 500;
    color: var(--gold-mid);
  }
</style>
</head>
<body>
  <main class="canvas">
    <section class="tube">
      <div class="tube-opening"></div>
      <div class="brand-seal">
        <span class="brand-name">miren</span>
      </div>
      <div class="product-band">
        <span class="product-name">CBD RICH HEMP FLOWER</span>
      </div>
      <div class="leaf-art" role="img" aria-label="Gold foil plant illustration"></div>
      <p class="website">www.dolvik.eu</p>
    </section>
  </main>
</body>
</html>
```